Welding company needs a business card

We are looking for a logo and business card.

Contact Information for Business Card

418 Cobblestone Lane
Harlow Falls, OH 44811
410-555-0173
Rmfabworksco@quorvamail.com

```html
<!DOCTYPE html>
<html lang="en">
<head>
<meta charset="utf-8">
<title>RM Fab Works – Business Card</title>
<link href="https://fonts.googleapis.com/css2?family=Hind:wght@500;600&display=swap" rel="stylesheet">
<style>
  :root {
    --paper: #ffffff;
    --card-dark: #07080c;
    --weld-blue: #3d7fc4;
    --spark-orange: #d9772e;
    --panel-yellow: #f6d40c;
    --band-gray: #4a4a4a;
    --ink: #111111;
  }
  html, body {
    margin: 0;
    width: 1200px;
    height: 720px;
    overflow: hidden;
    background: var(--paper);
  }
  .canvas {
    position: relative;
    width: 1200px;
    height: 720px;
    font-family: "Hind", sans-serif;
    color: var(--ink);
  }
  .card-art {
    position: absolute;
    left: 0;
    top: 0;
  }
  .brand {
    position: absolute;
    left: 827px;
    top: 217px;
    width: 240px;
    height: 40px;
    display: flex;
    align-items: center;
    justify-content: center;
    gap: 12px;
  }
  .brand-dot {
    width: 20px;
    height: 20px;
    border-radius: 50%;
    background: var(--ink);
  }
  .brand-name {
    font-size: 32px;
    font-weight: 600;
    line-height: 1;
    color: var(--ink);
  }
  .contact-icon {
    position: absolute;
    fill: none;
    stroke: var(--ink);
    stroke-width: 2;
    stroke-linecap: round;
    stroke-linejoin: round;
  }
  .contact-text {
    position: absolute;
    white-space: nowrap;
  }
  .address-icon { left: 651px; top: 391px; }
  .address-text {
    left: 711px;
    top: 391px;
    font-size: 30px;
    line-height: 38px;
    font-weight: 500;
  }
  .phone-icon { left: 659px; top: 479px; }
  .phone-text {
    left: 709px;
    top: 477px;
    font-size: 25px;
    line-height: 34px;
    font-weight: 600;
  }
  .email-icon { left: 654px; top: 526px; }
  .email-text {
    left: 706px;
    top: 524px;
    font-size: 25px;
    line-height: 34px;
    font-weight: 600;
  }
</style>
</head>
<body>
<div class="canvas">
  <svg class="card-art" width="1200" height="720" viewBox="0 0 1200 720">
    <defs>
      <radialGradient id="weldGlow" cx="0.38" cy="0.38" r="0.5">
        <stop offset="0" stop-color="var(--weld-blue)" stop-opacity="0.9"/>
        <stop offset="0.25" stop-color="#1d3a66" stop-opacity="0.7"/>
        <stop offset="0.6" stop-color="#0d1424"/>
        <stop offset="1" stop-color="var(--card-dark)"/>
      </radialGradient>
      <radialGradient id="sparkGlow" cx="0.4" cy="0.52" r="0.12">
        <stop offset="0" stop-color="var(--spark-orange)" stop-opacity="0.55"/>
        <stop offset="1" stop-color="var(--spark-orange)" stop-opacity="0"/>
      </radialGradient>
    </defs>
    <g class="photo-area" role="img" aria-label="Photo of a welder in a helmet working, with blue arc light and sparks">
      <rect x="42" y="41" width="1118" height="639" fill="url(#weldGlow)"/>
      <rect x="42" y="41" width="1118" height="639" fill="url(#sparkGlow)"/>
    </g>
    <polygon class="accent-band" points="739,37 1160,37 1160,661 367,661" fill="var(--band-gray)"/>
    <polygon class="info-panel" points="778,37 1160,37 1160,641 417,641" fill="var(--panel-yellow)"/>
  </svg>

  <div class="brand">
    <span class="brand-dot"></span>
    <span class="brand-name">RM Fab Works</span>
  </div>

  <svg class="contact-icon address-icon" width="26" height="36" viewBox="0 0 26 36">
    <path d="M13 33 C13 33 3 20 3 12 A10 10 0 0 1 23 12 C23 20 13 33 13 33 Z"/>
    <circle cx="13" cy="12" r="4"/>
  </svg>
  <div class="contact-text address-text">418 Cobblestone Lane<br>Harlow Falls, OH 44811</div>

  <svg class="contact-icon phone-icon" width="30" height="30" viewBox="0 0 30 30">
    <path d="M8 3 L12 9 L9.5 12 C11 15.5 14.5 19 18 20.5 L21 18 L27 22 L24.5 26.5 C15 27 3 15 3.5 5.5 Z"/>
    <path d="M18 3 A9 9 0 0 1 27 12"/>
    <path d="M18 8 A4 4 0 0 1 22 12"/>
  </svg>
  <div class="contact-text phone-text">410-555-0173</div>

  <svg class="contact-icon email-icon" width="34" height="30" viewBox="0 0 34 30">
    <path d="M3 11 L17 2 L31 11 V27 H3 Z"/>
    <path d="M3 11 L17 20 L31 11"/>
    <path d="M3 27 L13 18 M31 27 L21 18"/>
    <path d="M10 8 H24 M12 12 H22"/>
  </svg>
  <div class="contact-text email-text">Rmfabworksco@quorvamail.com</div>
</div>
</body>
</html>
```